依頼詳細
用紙横向き・横書きレイアウトでお願いします。

素材としてロゴデータを添付いたします。
ピクチャロゴとテキストロゴとのサイズのバランスは適宜ご調整してください。
(素材データはテキストが小さい気がします)

また顔写真を入れたいので、納品ファイルには後で写真と置き換える長方形オブジェクト(横12mm×縦15mm)を入れてください。

フォントはsans-serif系が希望です。
記載項目
情報の並び順としては下記のとおりで、適宜レイアウトをお願いします。

・不動産の「売りたい」「買いたい」をつなぐパートナー(←色指定:全体:ロゴのネイビー/「売りたい」:黄緑/「買いたい」:オレンジ)
・RMTリンクス(※ロゴ素材使用)
・土地・建物 買取販売・売買仲介

・店長 宅地建物取引士
・森野 達夫
・顔写真代用オブジェクト
・携帯:080-3917-6042
・メール:t-morino@rmt-links.example.jp

・〒000-0000
・群馬県みどり市大間々町桐原1042-7
・TEL:0277-00-4861
・FAX:0277-00-4869
・HP:http://rmt-links.example.jp
希望イメージ
シンプル 複雑
単色 カラフル
暗い 明るい
日常 高級
遊び心 厳粛
未来的 伝統的
女性的 男性的
希望する色
青系、水色系
納品ファイル
• 高解像度JPG (.jpg)
• イラストレーター形式 (.ai)
補足説明
.aiファイルでは、テキストは全てアウトライン化してください。

```html
<!DOCTYPE html>
<html lang="ja">
<head>
<meta charset="utf-8">
<title>RMTリンクス 名刺</title>
<link rel="stylesheet" href="https://fonts.googleapis.com/css2?family=Noto+Sans+JP:wght@400;500;700;900&display=swap">
<style>
  :root {
    --navy: #2d4c8c;
    --ink: #333333;
    --muted: #555555;
    --rule: #9a9a9a;
    --lime: #8cc63f;
    --orange: #f08c1e;
    --paper: #ffffff;
    --stage: #ffffff;
  }
  * { margin: 0; padding: 0; box-sizing: border-box; }
  html, body {
    width: 900px; height: 1200px; overflow: hidden;
    background: var(--stage);
    font-family: "Noto Sans JP", sans-serif;
    color: var(--ink);
  }
  .card {
    position: absolute; left: 60px; width: 780px; height: 472px;
    box-shadow: 0 2px 8px rgba(0,0,0,0.18);
  }
  .card--front { top: 110px; background: var(--paper); }
  .card--back { top: 650px; background: var(--navy); color: #fff; }

  /* front */
  .portrait {
    position: absolute; left: 112px; top: 224px; width: 76px; height: 95px;
    background: linear-gradient(160deg, #d9dde3, #8d96a3);
  }
  .title { position: absolute; left: 300px; top: 204px; font-size: 11px; letter-spacing: 0.25em; color: var(--muted); }
  .name { position: absolute; left: 290px; top: 224px; font-size: 25px; font-weight: 500; letter-spacing: 0.3em; }
  .name-rule { position: absolute; left: 90px; top: 270px; width: 360px; height: 1px; background: var(--rule); }
  .contact { position: absolute; left: 290px; font-size: 12px; color: var(--muted); display: flex; align-items: center; gap: 8px; }
  .contact--phone { top: 287px; }
  .contact--mail { top: 309px; }
  .contact svg { width: 12px; height: 12px; fill: var(--muted); }

  .brand { position: absolute; display: flex; align-items: center; gap: 10px; color: var(--navy); font-weight: 900; }
  .card--front .brand { left: 556px; top: 262px; font-size: 30px; }
  .brand-dot { width: 22px; height: 22px; border-radius: 50%; background: var(--navy); }

  .tagline { position: absolute; left: 0; right: 0; top: 352px; text-align: center; font-size: 20px; font-weight: 700; color: var(--navy); letter-spacing: 0.04em; }
  .tagline .sell { color: var(--lime); }
  .tagline .buy { color: var(--orange); }

  /* back */
  .card--back .brand { left: 0; right: 0; top: 150px; justify-content: center; color: #fff; font-size: 44px; }
  .card--back .brand-dot { width: 32px; height: 32px; background: #fff; }
  .office { position: absolute; top: 340px; font-size: 13px; line-height: 1.7; letter-spacing: 0.08em; }
  .office--address { left: 240px; }
  .office--lines { left: 525px; }
  .web { position: absolute; left: 0; right: 0; top: 400px; text-align: center; font-size: 16px; letter-spacing: 0.12em; font-weight: 500; }
</style>
</head>
<body>
  <section class="card card--front">
    <div class="portrait" role="img" aria-label="担当者の顔写真が入る枠"></div>
    <p class="title">宅地建物取引士</p>
    <p class="name">森野 達夫</p>
    <div class="name-rule"></div>
    <p class="contact contact--phone">
      <svg viewBox="0 0 24 24"><path d="M6.6 10.8a15.1 15.1 0 0 0 6.6 6.6l2.2-2.2a1 1 0 0 1 1-.25 11.4 11.4 0 0 0 3.6.57 1 1 0 0 1 1 1V20a1 1 0 0 1-1 1A17 17 0 0 1 3 4a1 1 0 0 1 1-1h3.5a1 1 0 0 1 1 1 11.4 11.4 0 0 0 .57 3.6 1 1 0 0 1-.25 1z"/></svg>
      080-3917-6042
    </p>
    <p class="contact contact--mail">
      <svg viewBox="0 0 24 24"><path d="M2 5h20v14H2zm2 2v.5l8 5 8-5V7zm0 3v7h16v-7l-8 5z"/></svg>
      t-morino@rmt-links.example.jp
    </p>
    <div class="brand"><span class="brand-dot"></span>RMTリンクス</div>
    <p class="tagline">不動産の「<span class="sell">売りたい</span>」「<span class="buy">買いたい</span>」をつなぐパートナー</p>
  </section>

  <section class="card card--back">
    <div class="brand"><span class="brand-dot"></span>RMTリンクス</div>
    <p class="office office--address">〒000-0000<br>群馬県みどり市大間々町桐原1042-7</p>
    <p class="office office--lines">TEL　0277-00-4861<br>FAX　0277-00-4869</p>
    <p class="web">http://rmt-links.example.jp</p>
  </section>
</body>
</html>
```